Dance School poster for end of year dance concert for mainly young girls.

We need an A3 portrait poster for our end of year concert.
Designs are attached of posters from previous 2 years as a reference only.
The theme of our concert this year is "Let's Dance" which we want to convey a general feel of energy & fun with dance.
Dance styles in the concert include Jazz & Hip Hop.
Bright colors are preferred in the design.

Target Market(s)

The concert is attended by several hundred family & friends

Industry/Entity Type

Dance Studio

Requirements
Must have
• Must have
• Let's Dance
• BRK logo (file supplied)
• 'The Maribel Crowe Dancers' (font is Mistral)
• Date of the concert: Saturday 14th November 2015
• Pellow Theatre, Saint Fenwick College Dalebrook
Nice to have
• We like clean design with no cluttered imagery.

```html
<!DOCTYPE html>
<html lang="en">
<head>
<meta charset="utf-8">
<title>Let's Dance – The Maribel Crowe Dancers</title>
<link rel="stylesheet" href="https://fonts.googleapis.com/css2?family=Bebas+Neue&family=Anton&family=Kaushan+Script&display=swap">
<style>
  :root {
    --cyan: #1fd6f2;
    --blue: #2a4fd8;
    --violet: #6a22c8;
    --magenta: #d11d8a;
    --crimson: #e0233f;
    --ribbon: #d8161c;
    --ribbon-dark: #8e0b0f;
    --gold-light: #fff3b0;
    --gold: #f3c23a;
    --gold-deep: #a8701a;
    --white: #ffffff;
    --ink: #111111;
  }
  * { margin: 0; padding: 0; box-sizing: border-box; }
  html, body { width: 849px; height: 1200px; overflow: hidden; background: var(--white); }
  .poster {
    position: relative;
    width: 849px;
    height: 1200px;
    overflow: hidden;
    font-family: "Bebas Neue", "Oswald", sans-serif;
    color: var(--white);
  }
  .backdrop {
    position: absolute; inset: 0;
    background:
      radial-gradient(ellipse at 50% 45%, rgba(255,255,255,0.18), transparent 60%),
      linear-gradient(180deg, var(--cyan) 0%, var(--blue) 30%, var(--violet) 55%, var(--magenta) 78%, var(--crimson) 100%);
  }
  .frame {
    position: absolute; inset: 8px;
    border: 3px solid rgba(255,255,255,0.85);
    box-shadow: 0 0 0 2px rgba(0,0,0,0.15);
    pointer-events: none;
  }
  .brand-tab {
    position: absolute; left: 368px; top: 0;
    width: 119px; height: 58px;
    background: var(--white);
    display: flex; align-items: center; justify-content: center;
    box-shadow: 0 3px 8px rgba(0,0,0,0.3);
  }
  .brand-name {
    font-family: "Bebas Neue", sans-serif;
    font-size: 40px; color: var(--ink); letter-spacing: 2px;
  }
  .ribbon {
    position: absolute; left: 0; top: 56px; width: 849px; height: 70px;
  }
  .ribbon-title {
    position: absolute; left: 0; right: 0; top: 64px;
    text-align: center;
    font-family: "Kaushan Script", cursive;
    font-size: 30px; color: var(--white);
  }
  .presents {
    position: absolute; left: 0; right: 0; top: 128px;
    text-align: center; font-size: 36px; letter-spacing: 2px;
  }
  .headline {
    position: absolute; left: 0; right: 0; top: 250px;
    text-align: center;
    font-family: "Anton", sans-serif;
    line-height: 0.95;
    color: var(--gold);
    background: linear-gradient(180deg, var(--gold-light) 0%, var(--gold) 45%, var(--gold-deep) 100%);
    -webkit-background-clip: text; background-clip: text;
    -webkit-text-fill-color: transparent;
    filter: drop-shadow(3px 5px 0 rgba(90,45,5,0.8)) drop-shadow(0 0 18px rgba(255,220,120,0.5));
  }
  .headline-top { display: block; font-size: 150px; letter-spacing: 2px; }
  .headline-bottom { display: block; font-size: 178px; letter-spacing: 4px; }
  .rating {
    position: absolute; left: 150px; top: 575px; width: 550px; height: 110px;
  }
  .details {
    position: absolute; left: 0; right: 0; top: 795px;
    text-align: center;
    font-size: 72px; line-height: 62px; letter-spacing: 1px;
    text-shadow: 0 2px 6px rgba(0,0,0,0.35);
  }
</style>
</head>
<body>
<main class="poster">
  <div class="backdrop" role="img" aria-label="Bright glowing dot pattern fading from cyan through blue and violet to magenta and red"></div>
  <div class="frame"></div>

  <div class="brand-tab"><span class="brand-name">BRK</span></div>

  <svg class="ribbon" viewBox="0 0 849 70" aria-hidden="true">
    <polygon points="150,14 190,14 190,62 150,62 165,38" fill="var(--ribbon-dark)"/>
    <polygon points="699,14 659,14 659,62 699,62 684,38" fill="var(--ribbon-dark)"/>
    <rect x="180" y="6" width="489" height="50" fill="var(--ribbon)"/>
  </svg>
  <p class="ribbon-title">The Maribel Crowe Dancers</p>

  <p class="presents">Presents</p>

  <h1 class="headline">
    <span class="headline-top">LET'S</span>
    <span class="headline-bottom">DANCE</span>
  </h1>

  <svg class="rating" viewBox="0 0 550 110" aria-hidden="true">
    <defs>
      <linearGradient id="star-gold" x1="0" y1="0" x2="0" y2="1">
        <stop offset="0" stop-color="#fff3b0"/>
        <stop offset="0.5" stop-color="#f3c23a"/>
        <stop offset="1" stop-color="#a8701a"/>
      </linearGradient>
      <polygon id="star" points="0,-48 11,-15 46,-15 18,6 29,40 0,19 -29,40 -18,6 -46,-15 -11,-15"/>
    </defs>
    <use href="#star" x="55" y="48" fill="url(#star-gold)"/>
    <use href="#star" x="165" y="58" fill="url(#star-gold)"/>
    <use href="#star" x="275" y="62" fill="url(#star-gold)"/>
    <use href="#star" x="385" y="58" fill="url(#star-gold)"/>
    <use href="#star" x="495" y="48" fill="url(#star-gold)"/>
  </svg>

  <p class="details">
    Saturday 14th<br>
    of November 2015<br>
    @ Pellow Theatre,<br>
    Saint Fenwick College<br>
    Dalebrook
  </p>
</main>
</body>
</html>
```